Alcohol free flavoured Malt Drink Label design

we are beverage company producer our main brand is Brightwave, we are willing to produce Alcohol free flavoured Malt Drink, this product target new generation should be fresh colourful and modern, the name of the Malt drink is Zeal. so main brand is Brightwave and product name is ZEAL. the label size: 198mm X 66mm

Dear All
i changed the product name to NUR (means Crown ) this will add more ideas in the design . Thanks

```html
<!DOCTYPE html>
<html lang="en">
<head>
<meta charset="utf-8">
<title>NUR Malt Drink – Label Fronts</title>
<link rel="stylesheet" href="https://fonts.googleapis.com/css2?family=Alfa+Slab+One&family=Montserrat:wght@700;800&display=swap">
<style>
  :root {
    --stage: #f3efe9;
    --ink-indigo: #2e2496;
    --ink-cream: #efe8e6;
    --brand-white: #f4f1f1;
    --sun-yellow: #ecd21c;
    --amber: #e59a12;
    --lime-haze: #cfd84a;
    --aqua: #58c6d3;
    --ocean: #4a6db7;
    --tangerine: #e27a1c;
    --magenta: #e03f9e;
    --berry: #b8245e;
  }
  * { margin: 0; padding: 0; box-sizing: border-box; }
  html, body { width: 1200px; height: 960px; overflow: hidden; }
  body {
    background: var(--stage);
    display: flex;
    justify-content: center;
    align-items: center;
    gap: 60px;
  }
  .label-front {
    width: 420px;
    height: 860px;
    border-radius: 6px;
    overflow: hidden;
    position: relative;
    box-shadow: 0 10px 30px rgba(0,0,0,0.12);
  }
  .label-front--ocean {
    background:
      linear-gradient(90deg, rgba(226,122,28,0.55) 0%, rgba(226,122,28,0) 35%),
      linear-gradient(180deg, var(--amber) 0%, var(--sun-yellow) 28%, var(--lime-haze) 50%, var(--aqua) 72%, var(--ocean) 100%);
    color: var(--ink-indigo);
  }
  .label-front--berry {
    background:
      linear-gradient(90deg, rgba(184,36,94,0.35) 0%, rgba(184,36,94,0) 35%),
      linear-gradient(180deg, var(--amber) 0%, var(--sun-yellow) 25%, var(--tangerine) 52%, var(--berry) 70%, var(--magenta) 100%);
    color: var(--ink-cream);
  }
  .label-art { width: 100%; height: 100%; display: block; }
  .frame-line, .abv-ring { fill: none; stroke: currentColor; }
  .product-name {
    font-family: "Alfa Slab One", Georgia, serif;
    font-size: 170px;
    fill: currentColor;
  }
  .product-type {
    font-family: "Montserrat", Arial, sans-serif;
    font-weight: 800;
    font-size: 30px;
    letter-spacing: 6px;
    fill: currentColor;
  }
  .parent-brand {
    font-family: "Montserrat", Arial, sans-serif;
    font-weight: 800;
    font-size: 30px;
    fill: var(--brand-white);
  }
  .abv-value {
    font-family: "Montserrat", Arial, sans-serif;
    font-weight: 800;
    fill: currentColor;
  }
  .abv-value .abv-big { font-size: 56px; }
  .abv-value .abv-small { font-size: 30px; }
  .abv-caption {
    font-family: "Montserrat", Arial, sans-serif;
    font-weight: 800;
    font-size: 15px;
    letter-spacing: 3px;
    fill: currentColor;
  }
</style>
</head>
<body>

  <section class="label-front label-front--ocean" aria-label="NUR malt drink, ocean variant">
    <svg class="label-art" viewBox="0 0 420 860">
      <defs>
        <path id="abv-arc-ocean" d="M 152 722 A 58 58 0 0 0 268 722"/>
      </defs>
      <path class="frame-line" stroke-width="8" d="M 82 185 C 42 215 30 262 30 330 L 30 500 C 30 580 55 640 98 690"/>
      <path class="frame-line" stroke-width="8" d="M 338 185 C 378 215 390 262 390 330 L 390 500 C 390 580 365 640 322 690"/>
      <text class="product-name" x="210" y="470" text-anchor="middle" textLength="300" lengthAdjust="spacingAndGlyphs">NUR</text>
      <text class="product-type" x="213" y="532" text-anchor="middle">MALT DRINK</text>
      <text class="parent-brand" x="210" y="598" text-anchor="middle">Brightwave</text>
      <circle class="abv-ring" cx="210" cy="715" r="76" stroke-width="8"/>
      <text class="abv-value" x="210" y="728" text-anchor="middle"><tspan class="abv-small">0.</tspan><tspan class="abv-big">0</tspan><tspan class="abv-small">%</tspan></text>
      <text class="abv-caption"><textPath href="#abv-arc-ocean" startOffset="50%" text-anchor="middle">ALCOHOL</textPath></text>
    </svg>
  </section>

  <section class="label-front label-front--berry" aria-label="NUR malt drink, berry variant">
    <svg class="label-art" viewBox="0 0 420 860">
      <defs>
        <path id="abv-arc-berry" d="M 152 722 A 58 58 0 0 0 268 722"/>
      </defs>
      <path class="frame-line" stroke-width="8" d="M 82 185 C 42 215 30 262 30 330 L 30 500 C 30 580 55 640 98 690"/>
      <path class="frame-line" stroke-width="8" d="M 338 185 C 378 215 390 262 390 330 L 390 500 C 390 580 365 640 322 690"/>
      <text class="product-name" x="210" y="470" text-anchor="middle" textLength="300" lengthAdjust="spacingAndGlyphs">NUR</text>
      <text class="product-type" x="213" y="532" text-anchor="middle">MALT DRINK</text>
      <text class="parent-brand" x="210" y="598" text-anchor="middle">Brightwave</text>
      <circle class="abv-ring" cx="210" cy="715" r="76" stroke-width="8"/>
      <text class="abv-value" x="210" y="728" text-anchor="middle"><tspan class="abv-small">0.</tspan><tspan class="abv-big">0</tspan><tspan class="abv-small">%</tspan></text>
      <text class="abv-caption"><textPath href="#abv-arc-berry" startOffset="50%" text-anchor="middle">ALCOHOL</textPath></text>
    </svg>
  </section>

</body>
</html>
```